Buisness card

**Front Side:**

**[Your Company Logo]**
**Steadfast Upkeep Engineering**
*Keeping Your Equipment Running Smoothly*

**Contact Information:**
- **Name:** [dale Harwick
- **Title:** [owner
- **Phone:** [5073918246
- **Email:** dale@suevx.com

**Back Side:**

**Services Offered:**
- Routine Inspections
- Equipment Maintenance
- Emergency Repairs
- Consultation Services
- New installs
Tag line
Be proactive not reactive

```html
<!DOCTYPE html>
<html lang="en">
<head>
<meta charset="utf-8">
<title>Steadfast Upkeep Engineering – Business Card</title>
<link rel="stylesheet" href="https://fonts.googleapis.com/css2?family=Montserrat:wght@700;800&family=Roboto:wght@400;700&family=Tinos&display=swap">
<style>
  :root {
    --navy: #0a2f7a;
    --navy-deep: #06235f;
    --teal: #0e6c93;
    --cyan: #00c8f8;
    --red: #e8262d;
    --ink: #151515;
    --paper: #ffffff;
    --backdrop: #2c2d2f;
  }
  * { box-sizing: border-box; margin: 0; padding: 0; }
  html, body { width: 1200px; height: 1122px; overflow: hidden; }
  body {
    background: var(--backdrop);
    display: flex; flex-direction: column; align-items: center; justify-content: center;
    gap: 40px;
    font-family: "Roboto", Arial, sans-serif;
  }
  .card {
    position: relative;
    width: 900px; height: 514px;
    border-radius: 30px;
    overflow: hidden;
    background: var(--paper);
  }

  /* wordmark lockup */
  .wordmark {
    font-family: "Montserrat", Arial, sans-serif;
    font-weight: 800;
    color: var(--navy);
    line-height: 1.05;
  }
  .motto {
    font-family: "Montserrat", Arial, sans-serif;
    font-weight: 800;
    color: var(--ink);
    letter-spacing: 0.5px;
  }

  /* back side */
  .back-lockup {
    position: absolute; left: 60px; top: 34px;
    display: flex; align-items: center; gap: 26px;
  }
  .back-lockup .mark-dot {
    width: 120px; height: 120px; border-radius: 50%;
    background: var(--navy);
    flex: none;
  }
  .back-lockup .wordmark { font-size: 38px; }
  .back-lockup .motto { font-size: 20px; margin-top: 8px; }

  .services-band {
    position: absolute; left: 0; right: 0; top: 196px; bottom: 0;
    background: linear-gradient(100deg, var(--navy-deep) 0%, var(--teal) 48%, var(--navy) 100%);
    color: var(--paper);
    text-align: center;
  }
  .services-title {
    margin-top: 34px;
    font-family: "Montserrat", Arial, sans-serif;
    font-weight: 800; font-size: 32px; letter-spacing: 9px;
  }
  .services-list {
    list-style: none;
    margin-top: 18px;
    font-size: 25px; line-height: 1.45;
  }
  .services-list span + span::before { content: " • "; }
  .services-list li::before { content: "• "; }
  .proactive-stripe {
    position: absolute; left: 0; right: 0; top: 206px; height: 58px;
    background: var(--cyan);
    font-family: "Montserrat", Arial, sans-serif;
    font-weight: 800; font-size: 28px;
    display: flex; align-items: center; justify-content: center;
  }

  /* front side */
  .front-lockup { position: absolute; left: 60px; top: 46px; }
  .front-lockup .wordmark { font-size: 42px; }
  .front-lockup .motto { font-size: 23px; margin-top: 10px; }
  .front-dot {
    position: absolute; right: 70px; top: 40px;
    width: 300px; height: 300px; border-radius: 50%;
    background: var(--navy);
  }
  .contact { position: absolute; left: 60px; top: 250px; }
  .contact::before {
    content: ""; position: absolute; left: -60px; top: 12px;
    width: 14px; height: 70px; background: var(--navy);
  }
  .person-name { font-weight: 700; font-size: 36px; color: var(--navy); }
  .person-title { font-family: "Tinos", "Times New Roman", serif; font-size: 25px; color: var(--ink); margin-top: 4px; }
  .contact-line {
    display: flex; align-items: center; gap: 16px;
    font-size: 24px; color: var(--ink); margin-top: 10px;
  }
  .contact-line svg { width: 28px; height: 28px; flex: none; }
  .slogan-rule {
    position: absolute; left: 0; right: 0; top: 424px; height: 4px; background: var(--red);
  }
  .slogan-band {
    position: absolute; left: 0; right: 0; top: 434px; bottom: 0;
    background: linear-gradient(100deg, var(--navy-deep), var(--teal) 55%, var(--navy));
    color: var(--paper);
    font-family: "Montserrat", Arial, sans-serif;
    font-weight: 800; font-size: 32px;
    display: flex; align-items: center; justify-content: center;
  }
</style>
</head>
<body>

  <section class="card card-back" aria-label="Back of business card">
    <div class="back-lockup">
      <div class="mark-dot"></div>
      <div>
        <div class="wordmark">Steadfast Upkeep<br>Engineering</div>
        <div class="motto">BE PROACTIVE NOT REACTIVE</div>
      </div>
    </div>
    <div class="services-band">
      <h2 class="services-title">SERVICES OFFERED</h2>
      <ul class="services-list">
        <li>Routine Inspections • Equipment Maintenance</li>
        <li>Emergency Repairs • Consultation Services • New installs</li>
      </ul>
      <div class="proactive-stripe">Be proactive not reactive</div>
    </div>
  </section>

  <section class="card card-front" aria-label="Front of business card">
    <div class="front-lockup">
      <div class="wordmark">Steadfast Upkeep<br>Engineering</div>
      <div class="motto">BE PROACTIVE NOT REACTIVE</div>
    </div>
    <div class="front-dot"></div>
    <div class="contact">
      <div class="person-name">dale Harwick</div>
      <div class="person-title">Owner</div>
      <div class="contact-line">
        <svg viewBox="0 0 24 24" aria-hidden="true"><path fill="#0a2f7a" d="M6.6 10.8a15.1 15.1 0 0 0 6.6 6.6l2.2-2.2c.3-.3.7-.4 1-.2 1.1.4 2.3.6 3.6.6.6 0 1 .4 1 1V20c0 .6-.4 1-1 1A17 17 0 0 1 3 4c0-.6.4-1 1-1h3.5c.6 0 1 .4 1 1 0 1.3.2 2.5.6 3.6.1.3 0 .7-.2 1z"/></svg>
        <span>5073918246</span>
      </div>
      <div class="contact-line">
        <svg viewBox="0 0 24 24" aria-hidden="true"><rect x="2" y="5" width="20" height="14" rx="1.5" fill="#0a2f7a"/><path d="M3 6.5l9 7 9-7" fill="none" stroke="#fff" stroke-width="1.6"/></svg>
        <span>dale@suevx.com</span>
      </div>
    </div>
    <div class="slogan-rule"></div>
    <div class="slogan-band">Keeping Your Equipment Running Smoothly</div>
  </section>

</body>
</html>
```